Software Product Flyer Design

A established czech software company needs a marketing flyer to promote their software product and its modules.
The overall feel of the flyer must to be serious, but also eye-catching, enticing, clever and bold to attract customers.
Unifying graphic element is the new product logo.
The flyer would be A4, colour both sides and folded once (to give 4 pages of A5).
Title page - product logo with module name and module icon, short presentation of the product and list of its key features.
Inside pages - detailed informations with screenshots or graphical schemas.
Back side - informations about technical requirements and user support, contacts (address, phone, fax, e-mail, web pages - no social networks).
Product logo, module icon and some images attached.
Updates
Hello,
Reason: For organizational reasons we extending the deadline by 10 days.
FYI: We have uploaded the new ZIP file with previous version of our flyer.
Attached PDF file with text for inner pages.
Target Market(s)
Existing or new customers like municipalities, public authorities and nonprofit organizations.
Industry/Entity Type
Marketing
Requirements
Must have
- Winning designer must provide a template for Adobe InDesign based on his graphic design.
Avoid to using exotic fonts - in Czech we use Latin Extended characters (like áéěíýůčřžšťďň).
Nice to have
- Using graphic motif from product logo like as attached splash screen.

```html
<!DOCTYPE html>
<html lang="en">
<head>
<meta charset="utf-8">
<title>Noval – Module Flyer Cover</title>
<link rel="stylesheet" href="https://fonts.googleapis.com/css2?family=Arimo:wght@400;700&display=swap">
<style>
  :root {
    --backdrop: #e4e2de;
    --paper-light: #fbfbfb;
    --paper-mid: #e9eaeb;
    --band-dark: #3b3f45;
    --band-edge: #50555c;
    --ink: #4a4d52;
    --ink-soft: #6b6e73;
    --accent: #e0531f;
    --shot-frame: #d6d8db;
    --shot-fill: #f1f2f3;
    --icon-tone: #8a8fa0;
    --crayon-tone: #d48a2a;
  }
  * { box-sizing: border-box; margin: 0; padding: 0; }
  html, body {
    width: 1200px; height: 900px; overflow: hidden;
    background: var(--backdrop);
    font-family: "Arimo", Arial, sans-serif;
  }
  .canvas { position: relative; width: 1200px; height: 900px; }

  .flyer-cover {
    position: absolute; left: 310px; top: 40px;
    width: 580px; height: 820px;
    background: linear-gradient(120deg, var(--paper-light) 0%, var(--paper-mid) 55%, var(--paper-light) 100%);
    box-shadow: 0 6px 22px rgba(0,0,0,.18);
    overflow: hidden;
  }
  .side-band { position: absolute; inset: 0; width: 100%; height: 100%; }

  .brand {
    position: absolute; left: 136px; top: 62px;
    display: flex; align-items: center; gap: 14px;
  }
  .brand-mark { width: 26px; height: 26px; background: var(--accent); }
  .brand-name {
    font-weight: 700; font-size: 64px; line-height: 1;
    color: var(--ink); letter-spacing: -1px;
  }

  .module-title {
    position: absolute; left: 250px; top: 270px;
    color: var(--ink); font-weight: 700;
  }
  .module-icon {
    width: 36px; height: 40px; border-radius: 4px;
    background: linear-gradient(160deg, #c9ccd6, var(--icon-tone));
    margin-bottom: 6px;
  }
  .module-title-line { font-size: 36px; line-height: 1.05; }
  .module-title-sub { display: flex; align-items: flex-end; gap: 4px; }
  .module-title-small {
    font-size: 13px; line-height: 1.05; text-align: right; font-weight: 700;
    padding-bottom: 4px;
  }
  .module-title-big { font-size: 38px; line-height: 1; }

  .screenshots {
    position: absolute; left: 24px; top: 345px;
    display: flex; flex-direction: column; gap: 14px;
  }
  .screenshot {
    width: 178px; height: 86px;
    background: linear-gradient(180deg, var(--shot-fill), var(--shot-frame));
    border: 5px solid var(--shot-frame);
    box-shadow: 0 2px 5px rgba(0,0,0,.35);
  }

  .key-features {
    position: absolute; left: 290px; top: 610px; width: 250px;
    color: var(--ink);
  }
  .key-features-head {
    display: flex; align-items: center; gap: 10px;
    border-bottom: 2px solid var(--accent); padding-bottom: 4px;
  }
  .key-features-title { font-weight: 700; font-size: 22px; }
  .key-features-icon {
    width: 30px; height: 34px; border-radius: 6px;
    background: linear-gradient(150deg, #f0b25a, var(--crayon-tone));
  }
  .feature-list { list-style: none; margin-top: 10px; padding-bottom: 12px; border-bottom: 2px solid var(--accent); }
  .feature-item {
    display: flex; align-items: center; gap: 8px;
    font-weight: 700; font-size: 15px; line-height: 1.45; color: var(--ink);
  }
  .feature-item svg { flex: none; }
</style>
</head>
<body>
<main class="canvas">
  <article class="flyer-cover">
    <svg class="side-band" viewBox="0 0 580 820" aria-hidden="true">
      <defs>
        <linearGradient id="bandShade" x1="0" y1="0" x2="1" y2="0">
          <stop offset="0" stop-color="#34383d"/>
          <stop offset="1" stop-color="#454a51"/>
        </linearGradient>
      </defs>
      <polygon points="0,0 165,0 142,820 0,820" fill="url(#bandShade)"/>
      <line x1="165" y1="0" x2="142" y2="820" stroke="var(--band-edge)" stroke-width="2"/>
    </svg>

    <div class="brand">
      <span class="brand-mark"></span>
      <span class="brand-name">Noval</span>
    </div>

    <section class="module-title">
      <div class="module-icon" role="img" aria-label="Module icon: small address book with letter A"></div>
      <div class="module-title-line">Title Name</div>
      <div class="module-title-sub">
        <span class="module-title-small">of<br>The</span>
        <span class="module-title-big">MODULE</span>
      </div>
    </section>

    <div class="screenshots">
      <div class="screenshot" role="img" aria-label="Screenshot of the module data table"></div>
      <div class="screenshot" role="img" aria-label="Screenshot of the module record list"></div>
      <div class="screenshot" role="img" aria-label="Screenshot of the module settings window"></div>
      <div class="screenshot" role="img" aria-label="Screenshot of the module form view"></div>
    </div>

    <section class="key-features">
      <div class="key-features-head">
        <h2 class="key-features-title">Key Features</h2>
        <div class="key-features-icon" role="img" aria-label="Icon of two orange crayons"></div>
      </div>
      <ul class="feature-list">
        <li class="feature-item"><svg width="9" height="10" viewBox="0 0 9 10"><polygon points="0,0 9,5 0,10" fill="var(--ink)"/></svg>Here will go key feature</li>
        <li class="feature-item"><svg width="9" height="10" viewBox="0 0 9 10"><polygon points="0,0 9,5 0,10" fill="var(--ink)"/></svg>Here will go key feature</li>
        <li class="feature-item"><svg width="9" height="10" viewBox="0 0 9 10"><polygon points="0,0 9,5 0,10" fill="var(--ink)"/></svg>Here will go key feature</li>
        <li class="feature-item"><svg width="9" height="10" viewBox="0 0 9 10"><polygon points="0,0 9,5 0,10" fill="var(--ink)"/></svg>Here will go key feature</li>
      </ul>
    </section>
  </article>
</main>
</body>
</html>
```